HR consultancy website - Wordpress Design Project

We need a wordpress design for a new company based in Belgium called Brivolane. We propose HR consultancy services focused on employees' engagement (motivation). We target corporations from 100 to 1000+ employees mainly in Europe.
We need a new design for our existing website (www.brivolane.eu).
We find the current design too static and outdated and we are looking for a more appealing look & feel.
Nevertheless, it has also to be sober.
The colours of the logo (dark blue, purple and light grey) should be preferrably used.
The content structure and the texts remain the same.

Target Market(s)

HR managers, general managers of SME's, higher education

Industry/Entity Type

It Company

Requirements
Must have
• No specific functionalities, except a contact form.

```html
<!DOCTYPE html>
<html lang="en">
<head>
<meta charset="utf-8">
<title>Brivolane – HR Consultancy</title>
<link rel="stylesheet" href="https://fonts.googleapis.com/css2?family=Bree+Serif&family=Open+Sans:wght@400;600&display=swap">
<style>
:root{
  --brand-blue:#0a4aa8;
  --brand-blue-dark:#063a8c;
  --brand-pink:#c8286a;
  --brand-pink-light:#eab2c8;
  --logo-grey:#c9c4bc;
  --text:#555555;
  --text-dark:#333333;
  --panel:#efefef;
  --rule:#e2e2e2;
}
*{margin:0;padding:0;box-sizing:border-box}
html,body{width:1200px;height:1052px;overflow:hidden}
body{
  position:relative;
  background:linear-gradient(180deg,#f6f6f6 0,#ffffff 320px);
  font-family:"Open Sans",Arial,sans-serif;
  color:var(--text);
}
.top-bar{position:absolute;left:0;top:0;width:1200px;height:6px;background:var(--brand-blue-dark)}
.brand{position:absolute;left:140px;top:58px;display:flex;align-items:center;gap:14px}
.brand-mark{width:22px;height:22px;border-radius:50%;background:var(--brand-blue)}
.brand-name{font-size:56px;font-weight:400;color:var(--logo-grey);letter-spacing:2px;line-height:1}
.contact-info{position:absolute;left:776px;top:28px;width:286px;font-size:14.5px;color:#888}
.contact-info .phone-icon{position:absolute;left:0;top:6px}
.contact-line{position:absolute;right:0;white-space:nowrap}
.contact-line.call{top:2px}
.contact-line.mail{top:30px;right:14px}
.contact-line strong{font-size:22px;font-weight:400;color:#111;margin-left:4px}
.contact-line a{color:var(--brand-pink);text-decoration:none}
.main-nav{position:absolute;top:122px;left:649px;display:flex;gap:2px}
.nav-tab{position:relative;width:136px;height:41px;display:flex;align-items:center;justify-content:flex-end;padding-right:14px;color:#fff;font-size:16px;text-decoration:none}
.nav-tab svg{position:absolute;left:0;top:0;z-index:-1}
.nav-tab span{width:100px;text-align:center}
.hero{position:absolute;left:140px;top:163px;width:922px;height:360px;background:#fff;box-shadow:0 0 6px rgba(0,0,0,.18)}
.hero-panel{position:absolute;left:10px;top:11px;width:902px;height:340px;background:var(--panel)}
.hero-copy{position:absolute;left:0;top:0;width:440px;text-align:center}
.hero-title{font-family:"Bree Serif",Georgia,serif;font-weight:400;font-size:44px;color:var(--brand-pink);margin-top:26px;line-height:52px}
.hero-rule{width:344px;height:1px;background:#dcdcdc;margin:14px auto 0 52px}
.hero-tagline{font-size:21.5px;font-weight:600;color:var(--text-dark);line-height:29px;margin-top:26px;margin-left:12px}
.hero-button{display:inline-block;margin-top:36px;margin-left:-16px;width:146px;height:34px;border-radius:17px;background:var(--brand-pink-light);color:#fff;font-family:"Bree Serif",Georgia,serif;font-size:19px;line-height:34px;text-decoration:none}
.hero-photo{position:absolute;left:420px;top:0;width:482px;height:340px;background:linear-gradient(135deg,#dfe6ee 0,#f3f5f8 55%,#e4e8ec 100%)}
.features{position:absolute;left:140px;top:540px;width:922px;height:216px;display:flex}
.feature{position:relative;width:234px;padding-right:14px}
.feature + .feature{border-left:1px solid var(--rule);padding-left:0}
.feature:nth-child(2),.feature:nth-child(3),.feature:nth-child(4){width:235px}
.feature-head{position:relative;height:48px;margin-top:25px}
.feature-head svg{position:absolute;left:0;top:0}
.feature-title{position:absolute;left:55px;top:4px;font-family:"Bree Serif",Georgia,serif;font-size:29px;font-weight:400;color:#fff;line-height:36px}
.feature-num{position:absolute;left:3px;top:1px;width:40px;height:40px;border-radius:50%;background:var(--brand-blue-dark);border:3px solid #fff;box-shadow:0 0 3px rgba(0,0,0,.4);color:#fff;font-size:24px;line-height:34px;text-align:center}
.feature p{font-size:15px;line-height:20.6px;text-align:center;margin:24px 6px 0 6px;color:var(--text)}
.feature + .feature .feature-head{margin-left:9px}
.cta{position:absolute;left:140px;top:810px;width:922px;height:90px;background:linear-gradient(180deg,#ededed 0,#fafafa 55%,#fff 100%)}
.cta-title{position:absolute;top:30px;width:100%;text-align:center;font-family:"Bree Serif",Georgia,serif;font-weight:400;font-size:24px;color:#555}
.cta-button{position:absolute;left:492px;top:896px;width:220px;height:70px;border-radius:35px;background:linear-gradient(180deg,#9a9a9a 0,#4a4a4a 45%,#111 52%,#1a1a1a 100%);border:2px solid #d9d9d9;box-shadow:0 3px 6px rgba(0,0,0,.35);color:#fff;font-family:"Bree Serif",Georgia,serif;font-size:24px;line-height:66px;text-align:center;text-decoration:none}
.footer-rule{position:absolute;left:140px;top:1006px;width:922px;height:1px;background:var(--rule)}
.copyright{position:absolute;top:1020px;width:1200px;text-align:center;font-size:15px;color:#555}
</style>
</head>
<body>
<div class="top-bar"></div>

<header>
  <div class="brand"><span class="brand-name">Brivolane</span><span class="brand-mark"></span></div>
  <div class="contact-info">
    <svg class="phone-icon" width="46" height="54" viewBox="0 0 46 54" aria-hidden="true">
      <path d="M10 4 C2 6 2 22 6 32 C10 42 18 48 26 46 L28 40 L21 35 L17 39 C13 35 11 27 11 20 L17 18 L16 9 Z" fill="none" stroke="#222" stroke-width="2.5" stroke-linejoin="round"/>
      <path d="M26 46 C34 44 40 40 44 34" fill="none" stroke="#222" stroke-width="2"/>
    </svg>
    <div class="contact-line call">Contact us on<strong>(02) 5820 3917</strong></div>
    <div class="contact-line mail">or email us <a href="#">hello@brivolane.eu</a></div>
  </div>
  <nav class="main-nav">
    <a class="nav-tab" href="#"><svg width="136" height="41"><path d="M0 41 C12 41 14 0 30 0 H136 V41 Z" fill="#0a4aa8"/></svg><span>Our Mission</span></a>
    <a class="nav-tab" href="#"><svg width="136" height="41"><path d="M0 41 C12 41 14 0 30 0 H136 V41 Z" fill="#0a4aa8"/></svg><span>About</span></a>
    <a class="nav-tab" href="#"><svg width="136" height="41"><path d="M0 41 C12 41 14 0 30 0 H136 V41 Z" fill="#0a4aa8"/></svg><span>Contact</span></a>
  </nav>
</header>

<section class="hero">
  <div class="hero-panel">
    <div class="hero-copy">
      <h1 class="hero-title">Brivolane</h1>
      <div class="hero-rule"></div>
      <p class="hero-tagline">FOSTER PERFORMANCE<br>BY<br>ENGAGING EMPLOYEES</p>
      <a class="hero-button" href="#">Our Mission</a>
    </div>
    <div class="hero-photo" role="img" aria-label="Photo of a business team standing in front of a faint world map"></div>
  </div>
</section>

<section class="features">
  <article class="feature">
    <div class="feature-head">
      <svg width="220" height="48"><defs><linearGradient id="rib" x1="0" y1="0" x2="0" y2="1"><stop offset="0" stop-color="#d84b86"/><stop offset="1" stop-color="#b81f5e"/></linearGradient></defs><path d="M20 2 H208 L218 21 L208 40 H20 Z" fill="url(#rib)"/><path d="M30 40 H200 L196 46 H40 Z" fill="#000" opacity=".08"/></svg>
      <span class="feature-num">1</span><h2 class="feature-title">Evaluation</h2>
    </div>
    <p>Only between 13 and 21% of employees are actively engaged in their job.</p>
  </article>
  <article class="feature">
    <div class="feature-head">
      <svg width="220" height="48"><path d="M20 2 H208 L218 21 L208 40 H20 Z" fill="url(#rib)"/><path d="M30 40 H200 L196 46 H40 Z" fill="#000" opacity=".08"/></svg>
      <span class="feature-num">2</span><h2 class="feature-title">Strategy</h2>
    </div>
    <p>Brivolane helps corporate leaders get the best contribu&shy;tion from employees.</p>
  </article>
  <article class="feature">
    <div class="feature-head">
      <svg width="220" height="48"><path d="M20 2 H208 L218 21 L208 40 H20 Z" fill="url(#rib)"/><path d="M30 40 H200 L196 46 H40 Z" fill="#000" opacity=".08"/></svg>
      <span class="feature-num">3</span><h2 class="feature-title">Process</h2>
    </div>
    <p>Our ERM tool creates an HR engagement cycle to encour&shy;age line managers to take ini&shy;tiatives and to enhance the engagement of their team members.</p>
  </article>
  <article class="feature">
    <div class="feature-head">
      <svg width="220" height="48"><path d="M20 2 H208 L218 21 L208 40 H20 Z" fill="url(#rib)"/><path d="M30 40 H200 L196 46 H40 Z" fill="#000" opacity=".08"/></svg>
      <span class="feature-num">4</span><h2 class="feature-title">Impact</h2>
    </div>
    <p>Our ERM tool measures impact by creating an index which can then be used for comparison over time.</p>
  </article>
</section>

<section class="cta">
  <h2 class="cta-title">Boost Your Company's Performance!</h2>
</section>
<a class="cta-button" href="#">Contact Us</a>

<footer>
  <div class="footer-rule"></div>
  <p class="copyright">Copyright © 2012 Brivolane. All Rights Reserved.</p>
</footer>
</body>
</html>
```